Flyer-Design für Vantro Summit
Zielgruppe
TV-Mediaagentur -> Spezialisierung auf Direct Response TV Werbung von E-Commerce Unternehmen
Aufgabenstellung
Flyer sollen auf einer Konferenz an Fachpersonal verteilt werden - wir haben auf dieser Konferenz einen kleinen Messestand.
Die Information muss somit schnell verstanden werden und der Flyer soll das Fachpersonal zu unserem Stand führen.
Bisherige unausgereifte Vorstellung.
Format: ca. A6 quer
Vorderseite: Logo zentriert groß / Logo Q8 Vorderseite- oder Rückseite unten / Standinformationen unten mittig / drum herum auf der Vorderseite Keywords wie z.B. "Direct Response Mediaagentur / Potential / Customer Journey Analysen / Profitabilität / Traffic / Umsatzsteigerung / KPI / TV Kampagnen / Werbewirkung / Brand Awareness /ROI / Know-How / Strategie / Planung / Kreation"
Rückseite: Etwas mehr Beschreibung zu uns, aber eben nicht zu viel Text.
Das ist unser Beschreibungstext bei der Konferenz:
https://www.q8-runde.de/q8_company/drtv-agency/

```html
<!DOCTYPE html>
<html lang="de">
<head>
<meta charset="utf-8">
<title>kanalpuls.agency – Flyer Rückseite</title>
<link rel="stylesheet" href="https://fonts.googleapis.com/css2?family=Exo+2:wght@400&display=swap">
<style>
  :root {
    --paper: #dadada;
    --band-grey-light: #e4e4e4;
    --band-grey-dark: #cfcfcf;
    --ink: #1f1f1f;
    --brand-blue: #1c6fb9;
    --band-blue: #2a7bbd;
    --band-blue-light: #4f93cc;
  }
  * { margin: 0; padding: 0; box-sizing: border-box; }
  html, body { width: 1200px; height: 851px; overflow: hidden; background: var(--paper); }
  .flyer-back {
    position: relative;
    width: 1200px;
    height: 851px;
    background: var(--paper);
    font-family: "Exo 2", sans-serif;
    color: var(--ink);
    overflow: hidden;
  }
  .keyword-band { position: absolute; left: 0; width: 1200px; }
  .keyword-band--top {
    top: 0;
    height: 122px;
    background: linear-gradient(100deg, var(--band-grey-dark) 0%, var(--band-grey-light) 45%, var(--band-grey-dark) 100%);
  }
  .keyword-band--bottom {
    top: 717px;
    height: 134px;
    background: linear-gradient(100deg, var(--band-blue) 0%, var(--band-blue-light) 50%, var(--band-blue) 100%);
  }
  .site-url {
    position: absolute;
    right: 74px;
    top: 96px;
    font-size: 25px;
    color: var(--brand-blue);
    letter-spacing: 0.2px;
  }
  .agency-copy {
    position: absolute;
    left: 49px;
    top: 168px;
    font-size: 22.6px;
    line-height: 27.5px;
    white-space: nowrap;
  }
  .agency-copy p + p { margin-top: 27.5px; }
</style>
</head>
<body>
<main class="flyer-back">

  <div class="keyword-band keyword-band--top" role="img" aria-label="Hellgraues Band mit schräg gesetzten Schlagworten wie Potential, Profitabilität, ROI, Planung, Know-How und Kreation"></div>

  <div class="site-url">www.kanalpuls.agency</div>

  <section class="agency-copy">
    <p>kanalpuls.agency ist eine inhabergeführte und unabhängige Direct Response Mediaagentur. Wir planen,<br>
    kreieren, analysieren und steuern für unsere Kunden aus dem E-Commerce Umfeld erfolgreiche<br>
    TV-Kommunikationskonzepte mit dem Ziel eines hochgradig positiven ROI´s bei gleichzeitiger<br>
    Stärkung der Brand Awareness.</p>
    <p>Abgestimmt auf Ihre Strategie und Zielgruppe helfen wir Ihnen, mit unserem Partnernetzwerk, einen<br>
    aussagekräftigen und performancestarken TV-Spot zu erstellen, der beste Kampagnenergebnisse erzielt.</p>
    <p>Durch unser weitverzweigtes Medianetzwerk können wir für unsere Kunden außerordentliche<br>
    Konditionen erzielen. Dazu kommt unser spezielles Know-how der Branche, welches wir durch unsere<br>
    langjährige Tätigkeit bei führenden E-Commerce-Unternehmen erwerben konnten.</p>
    <p>Schwerpunkt unserer Arbeit liegt in der datenbasierten, algorithmusgesteuerten Optimierung der TV<br>
    Kampagnen welches die gesamte Customer Journey betrachtet und das Budget aller Marketingkanäle<br>
    allokiert. Mit eigenen Trackingtechnologien, welche eine Vielzahl von Faktoren zur Beeinflussung der<br>
    Werbewirkung zur Prognosegenauigkeit nutzen, können wir – unter Berücksichtigung aller Online-<br>
    kanäle sowie des Customer Lifetime Values – Ihre TV-Kampagne bestens aussteuern. Wir analysieren<br>
    laufend, und identifizieren dabei KPIs, die zu Ihrer Strategie passen, um das Potenzial voll auszuschöpfen.</p>
  </section>

  <div class="keyword-band keyword-band--bottom" role="img" aria-label="Blaues Band mit schräg gesetzten Schlagworten wie Customer Journey, Direct Response, Strategie, TV Kampagnen, Brand Awareness und KPI"></div>

</main>
</body>
</html>
```